first fantastic look and impression

We are looking for a concept for letterhead, business card, emailfooter and template for invoices or offers for our company in the consultation business.
The dancer is a symbol who we are: it looks simple, but there is a lot of hard work and many years of training in this movement. The look is also what we want: elegant, modern, strong, with a touch of extravaganza
Target Market(s)
Hotelbusiness , Consulting
Font styles to use
Sans Serif
Other font styles liked:
- please give us a option we are open
Requirements
Must have
- We are not typical consultants but sparring partners and coaches for the hotel and that should also be expressed in the design. Maybe there is an icon that supports the whole thing. We are more modern and bolder than our industry colleagues.
we are modern, fresh, agile, fast
Nice to have
- a icon

```html
<!DOCTYPE html>
<html lang="de">
<head>
<meta charset="utf-8">
<title>Varga Partner – Visitenkarten</title>
<link rel="stylesheet" href="https://fonts.googleapis.com/css2?family=Roboto:wght@300;400;700&display=swap">
<style>
  :root{
    --bg:#d5dadb;
    --paper:#f3f2ee;
    --ink:#1d1d1f;
    --night:#111216;
    --light:#e9e9e6;
    --muted:#4a4a4c;
  }
  *{box-sizing:border-box;margin:0;padding:0}
  html,body{width:691px;height:1200px;overflow:hidden}
  body{background:var(--bg);font-family:"Roboto",Arial,sans-serif;color:var(--ink)}
  .set{height:600px;display:flex;align-items:center;justify-content:center;gap:22px}
  .set + .set{border-top:1px solid #cfd4d5}
  .card{width:316px;height:204px;position:relative;box-shadow:0 10px 24px rgba(0,0,0,.12)}
  .card--front{background:var(--paper);padding:26px 24px}
  .card--back{background:var(--night);display:flex;align-items:center;justify-content:center}
  .brand{font-weight:300;letter-spacing:.18em;text-transform:uppercase}
  .card--front .brand{position:absolute;right:22px;top:24px;font-size:13px;color:var(--ink)}
  .card--back .brand{font-size:22px;color:var(--light)}
  .contact{position:absolute;left:24px;bottom:22px}
  .contact__name{font-weight:700;font-size:11px;letter-spacing:.02em;text-transform:uppercase}
  .contact__rule{width:12px;height:1.5px;background:var(--ink);margin:9px 0 8px}
  .contact__list{list-style:none}
  .contact__list li{display:flex;align-items:center;gap:6px;font-size:9px;font-weight:300;color:var(--muted);line-height:13px}
  .icon{width:9px;height:9px;flex:none}
</style>
</head>
<body>
<svg width="0" height="0" style="position:absolute">
  <defs>
    <symbol id="i-pin" viewBox="0 0 10 10"><circle cx="5" cy="5" r="5" fill="#1d1d1f"/><path d="M5 2.2a1.8 1.8 0 0 1 1.8 1.8C6.8 5.4 5 7.6 5 7.6S3.2 5.4 3.2 4A1.8 1.8 0 0 1 5 2.2z" fill="#fff"/><circle cx="5" cy="4" r=".6" fill="#1d1d1f"/></symbol>
    <symbol id="i-phone" viewBox="0 0 10 10"><circle cx="5" cy="5" r="5" fill="#1d1d1f"/><path d="M3.3 2.6l1 1-.5.7a4 4 0 0 0 1.9 1.9l.7-.5 1 1-.6.8c-2 0-4.3-2.3-4.3-4.3z" fill="#fff"/></symbol>
    <symbol id="i-mobile" viewBox="0 0 10 10"><circle cx="5" cy="5" r="5" fill="#1d1d1f"/><rect x="3.6" y="2.3" width="2.8" height="5.4" rx=".5" fill="#fff"/><rect x="4.5" y="6.7" width="1" height=".4" fill="#1d1d1f"/></symbol>
    <symbol id="i-mail" viewBox="0 0 10 10"><circle cx="5" cy="5" r="5" fill="#1d1d1f"/><rect x="2.6" y="3.3" width="4.8" height="3.4" fill="#fff"/><path d="M2.6 3.3L5 5.2l2.4-1.9" fill="none" stroke="#1d1d1f" stroke-width=".5"/></symbol>
    <symbol id="i-web" viewBox="0 0 10 10"><circle cx="5" cy="5" r="5" fill="#1d1d1f"/><circle cx="5" cy="5" r="2.6" fill="none" stroke="#fff" stroke-width=".6"/><path d="M2.4 5h5.2M5 2.4c-1.2 1.4-1.2 3.8 0 5.2M5 2.4c1.2 1.4 1.2 3.8 0 5.2" fill="none" stroke="#fff" stroke-width=".5"/></symbol>
  </defs>
</svg>

<section class="set">
  <article class="card card--front">
    <div class="brand">Varga Partner</div>
    <div class="contact">
      <h2 class="contact__name">Lena Varga</h2>
      <div class="contact__rule"></div>
      <ul class="contact__list">
        <li><svg class="icon"><use href="#i-pin"/></svg>4820 Lindtal / Ahornweg 12</li>
        <li><svg class="icon"><use href="#i-phone"/></svg>+43 660 1234567</li>
        <li><svg class="icon"><use href="#i-mobile"/></svg>+43 660 7654321</li>
        <li><svg class="icon"><use href="#i-mail"/></svg>lv@vargapartner.com</li>
        <li><svg class="icon"><use href="#i-web"/></svg>vargapartner.com</li>
      </ul>
    </div>
  </article>
  <article class="card card--back">
    <div class="brand">Varga Partner</div>
  </article>
</section>

<section class="set">
  <article class="card card--front">
    <div class="brand">Varga Partner</div>
    <div class="contact">
      <h2 class="contact__name">Tobias Varga</h2>
      <div class="contact__rule"></div>
      <ul class="contact__list">
        <li><svg class="icon"><use href="#i-pin"/></svg>4820 Lindtal / Ahornweg 12</li>
        <li><svg class="icon"><use href="#i-mobile"/></svg>+43 660 7654321</li>
        <li><svg class="icon"><use href="#i-mail"/></svg>tv@vargapartner.com</li>
        <li><svg class="icon"><use href="#i-web"/></svg>vargapartner.com</li>
      </ul>
    </div>
  </article>
  <article class="card card--back">
    <div class="brand">Varga Partner</div>
  </article>
</section>
</body>
</html>
```